Realtor Just Listed Postcard Redesign

We need the existing postcard redesigned to fit on a 5x7 postcard.

Most importantly, we need the new postcard to be designed within a user friendly template system (PDF etc) that will allow us to change certain elements of the postcard (Front: photo Back: text information and photos). I've included additional previous design files as well.

Industry/Entity Type

Realtor

Requirements
Must have
• Template

```html
<!DOCTYPE html>
<html lang="en">
<head>
<meta charset="utf-8">
<title>Just Listed Postcard – Front and Back</title>
<link rel="stylesheet" href="https://fonts.googleapis.com/css2?family=Open+Sans:ital,wght@0,400;0,600;0,700;0,800;1,800&display=swap">
<style>
  :root {
    --red: #d8434b;
    --red-dark: #c3333c;
    --red-light: #e45a60;
    --blue: #2f5f93;
    --blue-dark: #23497a;
    --white: #ffffff;
    --ink: #1b1b1b;
    --stage: #2a2826;
    --photo-a: #8fa3b4;
    --photo-b: #c9c2b2;
  }
  * { box-sizing: border-box; margin: 0; padding: 0; }
  html, body { width: 900px; height: 1200px; overflow: hidden; }
  body { background: var(--stage); font-family: "Open Sans", sans-serif; position: relative; }
  .card { position: absolute; left: 70px; width: 760px; overflow: hidden; background: var(--red); box-shadow: 0 6px 18px rgba(0,0,0,.45); }
  .card-front { top: 30px; height: 585px; }
  .card-back { top: 645px; height: 525px; }
  .abs { position: absolute; }
  .bg { position: absolute; inset: 0; }
  .photo { position: absolute; background: linear-gradient(160deg, var(--photo-a), var(--photo-b)); border: 3px solid var(--white); }

  /* front */
  .headline { left: 0; top: 0; width: 760px; height: 92px; background: var(--red-dark); color: var(--white);
    font: italic 800 40px/92px "Open Sans", sans-serif; padding-left: 30px; }
  .headline .bang { position: absolute; right: 28px; top: -10px; font-size: 92px; line-height: 110px; font-style: normal; }
  .hero-photo { left: 15px; top: 108px; width: 255px; height: 210px; }
  .thumb-row { left: 15px; top: 326px; display: flex; gap: 5px; }
  .thumb-row .photo { position: static; width: 60px; height: 48px; border-width: 2px; }
  .photo-credit { left: 15px; top: 382px; width: 255px; font-size: 10px; color: var(--white); text-align: center; }
  .price-box { left: 282px; top: 114px; width: 240px; height: 52px; background: var(--white); color: var(--ink);
    font: 700 34px/52px "Open Sans", sans-serif; padding-left: 12px; }
  .area { left: 286px; top: 178px; color: var(--white); font: 600 26px/1.2 "Open Sans", sans-serif; }
  .specs { left: 286px; top: 232px; color: var(--white); font: 700 17px/1.3 "Open Sans", sans-serif; }
  .agent-photo { left: 530px; top: 100px; width: 230px; height: 310px; border: none;
    background: linear-gradient(170deg, #b9a48e, #4a3a32 60%, #1f1f24); }
  .agent-name { left: 515px; top: 414px; width: 210px; background: var(--white); color: var(--ink);
    font: 800 26px/1.15 "Open Sans", sans-serif; padding: 6px 12px; }
  .agent-contact { left: 530px; top: 494px; color: var(--white); font: 600 16px/1.45 "Open Sans", sans-serif; }
  .brand-box { left: 15px; top: 440px; width: 180px; height: 58px; background: var(--white); display: flex;
    align-items: center; justify-content: center; gap: 8px; color: var(--blue); font: 800 24px "Open Sans", sans-serif; }
  .brand-box .dot { width: 14px; height: 14px; border-radius: 50%; background: var(--blue); }
  .brand-note { left: 15px; top: 504px; width: 230px; color: var(--white); font-size: 10px; line-height: 1.35; }
  .website { color: var(--white); font: 700 16px "Open Sans", sans-serif; }
  .card-front .website { right: 30px; top: 553px; }

  /* back */
  .side-col { left: 0; top: 0; width: 170px; height: 525px; background: var(--white); }
  .tab-just-listed { left: 0; top: 12px; width: 170px; height: 38px; background: var(--blue); color: var(--white);
    font: 700 18px/38px "Open Sans", sans-serif; text-align: center; }
  .listing-photo { left: 22px; top: 60px; width: 126px; height: 110px; }
  .listing-facts { left: 12px; top: 180px; width: 154px; color: var(--red); font: 700 10px/1.35 "Open Sans", sans-serif; list-style: none; }
  .office-info { left: 12px; top: 380px; width: 154px; color: var(--ink); font-size: 9.5px; line-height: 1.35; }
  .office-info strong { color: var(--blue); font-size: 10.5px; }
  .invite { left: 200px; top: 10px; width: 400px; color: var(--white); text-align: center; }
  .invite h2 { font: 600 25px/1.2 "Open Sans", sans-serif; }
  .invite .address { font-size: 13px; margin-top: 4px; }
  .invite .dates { font: 800 22px/1.3 "Open Sans", sans-serif; }
  .follow { left: 620px; top: 66px; color: var(--white); font-size: 12px; text-align: center; width: 120px; }
  .follow .icons { display: flex; justify-content: center; gap: 6px; margin-top: 4px; }
  .follow .icons span { width: 24px; height: 24px; border-radius: 50%; background: var(--white); }
  .description { left: 200px; top: 165px; width: 340px; color: var(--white); font: 400 14px/1.36 "Open Sans", sans-serif; }
  .sold-panel { left: 565px; top: 150px; width: 180px; height: 320px; background: var(--white); }
  .sold-label { left: 565px; top: 158px; width: 180px; text-align: center; color: var(--blue); font: 700 18px "Open Sans", sans-serif; }
  .sold-a { left: 578px; top: 192px; width: 154px; height: 126px; }
  .sold-b { left: 578px; top: 330px; width: 154px; height: 126px; }
  .card-back .website { right: 24px; top: 490px; }
</style>
</head>
<body>

<section class="card card-front" aria-label="Postcard front">
  <svg class="bg" width="760" height="585" viewBox="0 0 760 585">
    <rect width="760" height="585" fill="var(--red)"/>
    <polygon points="0,585 0,420 300,585" fill="var(--blue)"/>
    <polygon points="330,585 760,300 760,585" fill="var(--red-light)"/>
    <polygon points="420,585 760,390 760,585" fill="var(--blue)"/>
  </svg>
  <div class="abs headline">You don’t want to miss this<span class="bang">!</span></div>

  <div class="photo hero-photo" role="img" aria-label="Exterior photo of the residential building"></div>
  <div class="abs thumb-row">
    <div class="photo" role="img" aria-label="Living room photo"></div>
    <div class="photo" role="img" aria-label="Kitchen photo"></div>
    <div class="photo" role="img" aria-label="Bedroom photo"></div>
    <div class="photo" role="img" aria-label="Bathroom photo"></div>
  </div>
  <p class="abs photo-credit">Stock photos used for illustration only</p>

  <div class="abs price-box">$295,000</div>
  <p class="abs area">965 sq. ft.</p>
  <p class="abs specs">Residential Attached<br>Bedrooms: 2, Bathrooms: 2</p>

  <div class="photo agent-photo" role="img" aria-label="Portrait of the realtor"></div>
  <div class="abs agent-name">REALTOR<br>MARCUS</div>
  <p class="abs agent-contact">(555) 318-0462<br>marcus@realtormarcus.com</p>

  <div class="abs brand-box"><span class="dot"></span>Summit</div>
  <p class="abs brand-note">Summit Select Realty<br>Each office independently owned and operated</p>
  <p class="abs website">www.realtormarcus.com</p>
</section>

<section class="card card-back" aria-label="Postcard back">
  <svg class="bg" width="760" height="525" viewBox="0 0 760 525">
    <rect width="760" height="525" fill="var(--red)"/>
    <polygon points="170,0 760,0 760,110 170,150" fill="var(--blue)"/>
    <polygon points="170,470 760,470 760,525 170,525" fill="var(--white)"/>
  </svg>
  <div class="abs side-col"></div>
  <div class="abs tab-just-listed">Just Listed</div>
  <div class="photo listing-photo" role="img" aria-label="Exterior photo of the listed building"></div>
  <ul class="abs listing-facts">
    <li>Price: $295,000</li>
    <li>Dwelling Type: Apartment/Condo</li>
    <li>Property Type: Residential Attached</li>
    <li>Home Style: Ground Level Unit</li>
    <li>Bedrooms: 2</li>
    <li>Status: Active</li>
    <li>Bathrooms: 2.0</li>
    <li>Year Built: 1999</li>
    <li>Floor Area: 965 sq. ft.</li>
  </ul>
  <p class="abs office-info"><strong>Summit Select Realty</strong><br>1200 Harbor St, Westport, BC V0V 0A0<br>Each Office Independently Owned &amp; Operated<br>This notice is not meant to disrupt any existing agency agreement</p>

  <div class="abs invite">
    <h2>You’re invited to an Open House</h2>
    <p class="address">410-220 Lakeview Way is showing on</p>
    <p class="dates">May 5th &amp; 6th, 2-4PM</p>
  </div>
  <div class="abs follow">Follow me on:
    <div class="icons"><span></span><span></span><span></span></div>
  </div>

  <p class="abs description">Beautiful garden level suite with private entrance at The Ashford. This cleverly distributed, bright 2 bedroom living space includes in-suite laundry and has an open concept gourmet kitchen with a breakfast bar and walnut cabinetry. The generous Master bedroom has ample closet space and a luxurious bathroom. The Ashford is known for its many amenities including a playground, outdoor pool, theatre room, huge clubhouse and more. Walking distance to public transportation, shopping and great restaurants.</p>

  <div class="abs sold-panel"></div>
  <p class="abs sold-label">Recently Sold:</p>
  <div class="photo sold-a" role="img" aria-label="Photo of a recently sold townhouse"></div>
  <div class="photo sold-b" role="img" aria-label="Photo of a recently sold condo building"></div>

  <p class="abs website" style="color: var(--blue);">www.realtormarcus.com</p>
</section>

</body>
</html>
```